Design a clean and bold corporate Presentation for Brand New Company

Task Outline
Create corporate presentation

Task Description
Creation of Powerpoint corporate presentation using the content below.

The presentation is 10 slides long.

PLEASE NOTE: THE FULL CONTENT AND STRUCTURE OF THE CORPORATE PRESENTATION ARE INCLUDED IN ATTACHMENT.

Corporate presentation
– structure is as attached in file titled “novaquill Corp Pres”.

We would like a clean, modern presentation with the use of graphics (not photos) to support key points. We need the graphics designed – NOT clip-art, as we aim to use these on the web-site (examples of preferred design below).

novaquill is a new start-up company where we aim to combine the best of recruitment and IT service delivery expertise to:

Offer access to the best possible resources in the UK and Globally, in a range of commercial models that offer cost savings and agility. Using best practice service delivery to assure quality.

Our foundations are outstanding employee satisfaction, and fantastic customer service.

Do’s
- Be bold ! Use clean design graphics to better highlight and explain products and capabilities in the corporate presentation
- Professional, contemporary and clean – our target market are new IT businesses that are web-savvy.
- Use single colour graphics
- Use a consistent theme through-out
- Establish a design that would translate easily to the web
- Establish a design that would translate into a Powerpoint template
- Use Calibri font

Don’ts
- Use generic photos e.g. “smiling IT professional” ;-)
- No cartoon graphics
- Use complex multi-colour graphics
- Use standard Powerpoint clip-art
- Create a large file
- Use animation / transitions

Output
Powerpoint file – 2011 but compatible with 2007

Deadline
+ 1 week from issue.

What is your industry?
IT Recruitment, Consulting, Professional Services

Target Market
• New customers - Our target market are high growth companies with a heavy reliance on IT, 50-250 employees, based in UK.
• Hiring candidates – IT professionals who are potential hiring candidates for our customers.
• Employees – typically graduates who will be looking for their first/second professional role

What design styles do you like that you would like to reflect in the design?
• http://www.qrtv.com/what-we-offer/
• http://www.brindle.io/platform-as-a-service/brindle-sky-harbor
• www.plume.com

Do you have any other info or links you want to share?
- Corporate presentation
- Logo image

Target Market(s)

Target Market

Industry/Entity Type

It Company

Font styles to use
Sans Serif

Colors
34a6d7
faa54b
d2a4cc
85acd3

Requirements
Must have
• Do’s
• - Be bold ! Use clean design graphics to better highlight and explain products and capabilities in the corporate presentation
• - Professional, contemporary and clean – our target market are new IT businesses that are web-savvy.
• - Use single colour graphics
• - Use a consistent theme through-out
• - Establish a design that would translate easily to the web
• - Establish a design that would translate into a Powerpoint template
• - Use Calibri font
Nice to have
• Use of transparent background imagery
Should not have
• Don’ts
• - Use generic photos e.g. “smiling IT professional” ;-)
• - No cartoon graphics
• - Use complex multi-colour graphics
• - Use standard Powerpoint clip-art
• - Create a large file
• - Use animation / transitions

```html
<!DOCTYPE html>
<html lang="en">
<head>
<meta charset="utf-8">
<title>Our Mission – novaquill</title>
<link rel="stylesheet" href="https://fonts.googleapis.com/css2?family=Carlito:wght@400;700&display=swap">
<style>
  :root {
    --brand-blue: #1f4a8f;
    --brand-orange: #f47b20;
    --body-grey: #666666;
    --tab-grey: #d9d9d9;
    --tab-edge: #bcbcbc;
    --page-white: #ffffff;
    --swoosh-grey: #ececec;
    --art-light: #f1f1f1;
    --art-warm: #ecd9d9;
  }
  * { box-sizing: border-box; margin: 0; padding: 0; }
  html, body { width: 1200px; height: 900px; overflow: hidden; }
  body { font-family: "Carlito", Calibri, Arial, sans-serif; background: var(--page-white); }

  .slide {
    position: relative;
    width: 1200px;
    height: 900px;
    overflow: hidden;
    background:
      radial-gradient(ellipse 900px 500px at 0% 30%, var(--swoosh-grey) 0%, rgba(236,236,236,0) 70%),
      radial-gradient(ellipse 700px 400px at 30% 75%, #f4f4f4 0%, rgba(244,244,244,0) 70%),
      linear-gradient(160deg, #f3f3f3 0%, var(--page-white) 55%);
  }
  .slide__swoosh { position: absolute; inset: 0; width: 1200px; height: 900px; }

  .title-tab {
    position: absolute;
    left: 0; top: 30px;
    width: 307px; height: 78px;
    background: linear-gradient(180deg, #eeeeee 0%, var(--tab-grey) 100%);
    border: 2px solid var(--tab-edge);
    border-left: none;
    border-radius: 0 18px 18px 0;
    box-shadow: 0 3px 8px rgba(0,0,0,0.15);
    display: flex; align-items: center;
    padding-left: 24px;
  }
  .title-tab__text {
    color: var(--brand-blue);
    font-weight: 700;
    font-size: 38px;
  }

  .mission { position: absolute; left: 123px; top: 222px; width: 760px; }
  .mission__lead {
    font-weight: 700;
    font-size: 31px;
    line-height: 42px;
    color: var(--brand-blue);
  }
  .mission__lead-accent { color: var(--brand-orange); }

  .mission__points { list-style: none; margin-top: 84px; margin-left: 47px; width: 640px; }
  .mission__point {
    position: relative;
    font-size: 25px;
    line-height: 43px;
    color: var(--body-grey);
    margin-bottom: 39px;
  }
  .mission__point::before {
    content: "";
    position: absolute;
    left: -40px; top: 12px;
    width: 20px; height: 20px;
    border-radius: 50%;
    background: var(--brand-orange);
  }
  .mission__highlight { color: var(--brand-blue); font-weight: 700; }

  .goal-illustration {
    position: absolute;
    left: 920px; top: 350px;
    width: 270px; height: 280px;
    border-radius: 16px;
    background: linear-gradient(180deg, var(--art-light) 0%, var(--art-light) 55%, var(--art-warm) 100%);
  }

  .footer-band {
    position: absolute;
    left: 0; bottom: 0;
    width: 1200px; height: 42px;
    background: var(--brand-orange);
    display: flex; align-items: center; justify-content: space-between;
    padding: 0 18px 0 12px;
  }
  .footer-band__copyright { color: var(--page-white); font-size: 19px; }
  .brand-name {
    display: flex; align-items: center; gap: 8px;
    color: var(--page-white);
    font-weight: 700;
    font-size: 28px;
  }
  .brand-name__dot { width: 14px; height: 14px; border-radius: 50%; background: var(--page-white); }
</style>
</head>
<body>
  <main class="slide">
    <svg class="slide__swoosh" viewBox="0 0 1200 900" aria-hidden="true">
      <path d="M0 180 C300 240 520 420 560 900 L0 900 Z" fill="#f6f6f6" opacity="0.8"/>
      <path d="M0 420 C200 460 420 600 480 900" fill="none" stroke="#e6e6e6" stroke-width="3"/>
      <path d="M120 0 C260 200 240 500 60 900" fill="none" stroke="#eeeeee" stroke-width="40" opacity="0.6"/>
    </svg>

    <header class="title-tab">
      <h1 class="title-tab__text">OUR MISSION</h1>
    </header>

    <section class="mission">
      <h2 class="mission__lead">Combine the best of<br>
        <span class="mission__lead-accent">recruitment and IT service delivery expertise to:</span>
      </h2>
      <ul class="mission__points">
        <li class="mission__point">Offer access to the best possible resources in the<br><span class="mission__highlight">UK and Globally</span>, in a range of commercial models<br>that offer cost savings and agility. Using best<br>practice service delivery to assure quality.</li>
        <li class="mission__point">Our foundations are outstanding employee<br>satisfaction, and fantastic customer service.</li>
      </ul>
    </section>

    <div class="goal-illustration" role="img" aria-label="Illustration of a white figure standing on a red and white target"></div>

    <footer class="footer-band">
      <span class="footer-band__copyright">Copyright text here</span>
      <span class="brand-name"><span class="brand-name__dot"></span>novaquill</span>
    </footer>
  </main>
</body>
</html>
```